Residential Remodeling Contractor needs updated business card

I need a new design for my business card.
Name of the company is Brookfell Construction. I need a card that commands presence, strength, integrity. I have been in business for 28 years. I am a Residential Remodeling Contractor that covers all aspects of a residential remodel and build.

```html
<!DOCTYPE html>
<html lang="en">
<head>
<meta charset="utf-8">
<title>Brookfell Construction – Business Card</title>
<link rel="stylesheet" href="https://fonts.googleapis.com/css2?family=Open+Sans:wght@400;600;700&display=swap">
<style>
  :root {
    --stage: #222222;
    --brand-blue: #213e7e;
    --paper: #ffffff;
    --soft-white: #d9deea;
    --card-w: 560px;
    --card-h: 320px;
  }
  * { box-sizing: border-box; margin: 0; padding: 0; }
  html, body {
    width: 1200px;
    height: 780px;
    overflow: hidden;
    background: var(--stage);
    font-family: "Open Sans", Arial, sans-serif;
  }
  .card-set {
    position: relative;
    width: 1200px;
    height: 780px;
    display: flex;
    align-items: center;
    justify-content: center;
    gap: 40px;
  }
  .card {
    position: relative;
    width: var(--card-w);
    height: var(--card-h);
    background: var(--brand-blue);
    overflow: hidden;
    box-shadow: 0 12px 30px rgba(0,0,0,.45);
  }
  .card__sweep {
    position: absolute;
    inset: 0;
    width: 100%;
    height: 100%;
  }
  .brand-name {
    position: absolute;
    color: var(--paper);
    font-family: "Open Sans", Arial, sans-serif;
    font-weight: 600;
    text-transform: uppercase;
    line-height: 1.05;
    letter-spacing: 0.04em;
  }
  .card--front .brand-name {
    left: 250px;
    top: 48px;
    font-size: 30px;
  }
  .card--front .brand-name span { display: block; font-size: 21px; letter-spacing: 0.07em; }
  .card--back .brand-name {
    left: 0;
    right: 0;
    top: 108px;
    text-align: center;
    font-size: 50px;
  }
  .card--back .brand-name span { display: block; font-size: 34px; letter-spacing: 0.09em; margin-top: 4px; }

  .person {
    position: absolute;
    right: 360px;
    top: 132px;
    text-align: right;
    color: var(--paper);
    white-space: nowrap;
  }
  .person__name { font-size: 22px; font-weight: 700; line-height: 1.1; }
  .person__first { font-weight: 600; color: var(--soft-white); }
  .person__title { font-size: 12px; font-weight: 400; margin-top: 4px; }

  .divider {
    position: absolute;
    left: 214px;
    top: 122px;
    width: 1.5px;
    height: 96px;
    background: var(--paper);
  }
  .contact-list {
    position: absolute;
    left: 232px;
    top: 140px;
    list-style: none;
    color: var(--paper);
    font-size: 14px;
    line-height: 22px;
  }
  .contact-list li { display: flex; align-items: center; gap: 8px; }
  .contact-list svg { width: 13px; height: 13px; flex: none; }

  .address {
    position: absolute;
    left: 34px;
    bottom: 24px;
    color: var(--brand-blue);
    font-size: 14px;
    line-height: 19px;
    font-weight: 400;
    white-space: nowrap;
  }
</style>
</head>
<body>
<main class="card-set">

  <section class="card card--front" aria-label="Card front with contact details">
    <svg class="card__sweep" viewBox="0 0 560 320" preserveAspectRatio="none" aria-hidden="true">
      <path d="M0,175 C80,235 300,262 560,268 L560,320 L0,320 Z" fill="var(--paper)"/>
      <path d="M8,168 C88,226 300,252 560,258" fill="none" stroke="#c9d1e6" stroke-opacity=".55" stroke-width="2"/>
    </svg>

    <div class="brand-name">Brookfell<span>Construction</span></div>

    <div class="person">
      <div class="person__name"><span class="person__first">Marta</span> Kovalenko</div>
      <div class="person__title">Managing Director</div>
    </div>

    <div class="divider"></div>

    <ul class="contact-list">
      <li>
        <svg viewBox="0 0 16 16" aria-hidden="true"><path fill="var(--soft-white)" d="M3.6 1.5l2.2 2.6-1.3 1.6c.9 2 2.4 3.5 4.3 4.4l1.6-1.3 2.6 2.2-1.3 2.3C6.8 13.2 2.8 9.2 1.4 2.8z"/></svg>
        (555) 014-2290
      </li>
      <li>
        <svg viewBox="0 0 16 16" aria-hidden="true"><rect x="1.5" y="3.5" width="13" height="9" fill="none" stroke="var(--soft-white)" stroke-width="1.6"/><path d="M1.5 3.5l6.5 5 6.5-5" fill="none" stroke="var(--soft-white)" stroke-width="1.6"/></svg>
        info@brookfellbuild.com
      </li>
      <li>
        <svg viewBox="0 0 16 16" aria-hidden="true"><circle cx="8" cy="8" r="6.3" fill="none" stroke="var(--soft-white)" stroke-width="1.5"/><ellipse cx="8" cy="8" rx="2.8" ry="6.3" fill="none" stroke="var(--soft-white)" stroke-width="1.2"/><path d="M1.7 8h12.6" stroke="var(--soft-white)" stroke-width="1.2"/></svg>
        www.brookfellbuild.com
      </li>
    </ul>

    <p class="address">418 Alder Ridge Rd. Suite 120 Denton, TX 76201</p>
  </section>

  <section class="card card--back" aria-label="Card back with company name">
    <div class="brand-name">Brookfell<span>Construction</span></div>
  </section>

</main>
</body>
</html>
```